Brochure Design Project

WE NEED A BROCHURE!!! - This should be easy and allows you to be creative! Corvane Nexus creates web and mobile portals for businesses in the health and wellness industry. The websites and mobile apps engage our clients' patients and consumers in health and wellness activities such as managing their conditions or losing weight. We leverage our large platform code-stack to build custom solutions for each client. We really love our website www.corvanenexus.com. So all we need is for someone to take that branding and create a 2-4 page brochure. The text is not that important as we can change it as needed. Mostly we just need the layout. We'd like to include the Zo Ka Lum colors and the JOURNAL font as included on our website.

• The 2 PDFs uploaded are 2 attempts that we aren't happy with but can be used as a reference only. Please be creative.

Must have the same branding language as our website www.corvanenexus.com - so that it looks like the same company.

Must have format/room for images. You can plug in stock photography if you'd like and we can buy or add in custom images later.

The font is JOURNAL for the zo/ka/lum. Other fonts are optional. Colors are:

Me – Green RGB 140, 188, 0
We – Blue RGB 11, 116, 187
Info – Orange RGB 237, 137, 33
Dark Gray – RGB 70, 80, 89
Med Gray – 114, 132, 154
Light Gray – 236, 238, 239

Thank you!

```html
<!DOCTYPE html>
<html lang="en">
<head>
<meta charset="utf-8">
<title>Corvane Nexus Brochure</title>
<link href="https://fonts.googleapis.com/css2?family=Kalam:wght@300;400&family=Open+Sans:wght@600;700&family=Arimo:wght@400;700&display=swap" rel="stylesheet">
<style>
  :root{
    --green:rgb(140,188,0);
    --blue:rgb(11,116,187);
    --orange:rgb(237,137,33);
    --magenta:#d42b9e;
    --dark-gray:rgb(70,80,89);
    --med-gray:rgb(114,132,154);
    --light-gray:rgb(236,238,239);
    --backdrop:#cfd1d3;
    --paper:#ffffff;
    --script:"Kalam",cursive;
    --brand:"Open Sans",sans-serif;
    --body:"Arimo",sans-serif;
  }
  *{box-sizing:border-box;margin:0;padding:0}
  html,body{width:1200px;height:793px;overflow:hidden;background:var(--backdrop)}
  .spread{position:relative;width:1200px;height:793px}
  .page{position:absolute;top:36px;width:540px;height:720px;background:var(--paper);box-shadow:0 2px 10px rgba(0,0,0,.15);overflow:hidden}
  .page--inside{left:60px}
  .page--cover{left:600px;border-left:1px solid #e3e4e5}

  /* inside page */
  .section-title{position:absolute;font-family:var(--script);font-weight:300;font-size:22px;letter-spacing:1px;line-height:1}
  .section-title--editions{left:40px;top:34px;color:var(--orange);width:130px}
  .section-title--why{left:40px;top:420px;color:var(--green)}
  .intro{position:absolute;left:40px;top:92px;width:250px;font:9px/1.3 var(--body);color:var(--dark-gray)}
  .lead{position:absolute;left:40px;top:200px;width:260px;font:12.5px/1.3 var(--body);color:var(--dark-gray)}
  .photo{position:absolute;left:318px;top:40px;width:190px;height:110px;border-radius:16px;background:linear-gradient(135deg,#9a9ea3,#4e5358 60%,#2f3236)}
  .editions{position:absolute;left:40px;top:244px;width:470px;height:96px}
  .edition{position:absolute;display:flex;align-items:center;gap:6px;font-family:var(--body);color:var(--dark-gray);white-space:nowrap}
  .edition__dot{width:26px;height:26px;border-radius:50%;flex:none}
  .edition__small{font-size:8px;font-weight:700;display:block}
  .edition__name{font-size:11.5px;display:block}
  .body-text{position:absolute;left:40px;width:460px;font-family:var(--body);color:var(--dark-gray);text-align:justify}
  .body-text--editions{top:340px;font-size:12.5px;line-height:1.35}
  .body-text--why{top:452px;font-size:9px;line-height:1.35}
  .swoosh{position:absolute;left:0;width:540px;height:40px}
  .brand-small{position:absolute;left:40px;top:562px;font:700 19px/1 var(--brand);color:var(--dark-gray);letter-spacing:-.5px}
  .contact{position:absolute;font:9px/1.3 var(--body);color:var(--dark-gray)}
  .contact__label{color:var(--green);font-weight:700;display:block}
  .contact--head{left:40px;top:588px}
  .contact--intl{left:200px;top:604px;padding-left:10px;border-left:1px solid var(--med-gray)}
  .contact-call{position:absolute;left:320px;top:572px;font:400 20px/1 var(--script);color:var(--green);white-space:nowrap}
  .web{position:absolute;left:330px;top:640px;padding-left:12px;border-left:1px solid var(--med-gray);font:400 15px/1.4 var(--script);color:var(--green);white-space:nowrap}

  /* cover */
  .brand-cover{position:absolute;left:60px;top:78px;font:700 38px/1 var(--brand);color:var(--dark-gray);letter-spacing:-1px}
  .tagline{position:absolute;left:40px;top:138px;width:470px;font:400 18px/1.35 var(--script);color:var(--green);text-align:right}
  .hero{position:absolute;left:130px;top:290px;width:300px;height:290px;border-radius:12px;background:radial-gradient(circle at 50% 45%,#b3d85a 0%,#9ccb3a 45%,#e9a45a 85%,#f3f4f1 100%)}
  .formula{position:absolute;right:44px;bottom:60px;text-align:right}
  .formula__word{font:400 26px/1 var(--script);color:var(--green);display:inline-flex;align-items:center;gap:6px}
  .formula__note{font:400 14px/1.2 var(--script);color:var(--dark-gray)}
</style>
</head>
<body>
<main class="spread">

  <section class="page page--inside">
    <h2 class="section-title section-title--editions">PLATFORM EDITIONS</h2>
    <p class="intro">The Corvane Nexus Platform is built on a modular, component-based architecture to allow deep customization and integration. The flexible structure enables us to bring our clients' visions to life in a cost effective and timely manner, while delivering solutions that are high-value for their customers and brands.</p>
    <div class="photo" role="img" aria-label="Photo of a woman touching a glowing digital interface"></div>
    <p class="lead">We offer specialized editions of our web and mobile platform that are market specific:</p>

    <div class="editions">
      <div class="edition" style="left:0;top:0"><span class="edition__dot" style="background:var(--blue)"></span><span><span class="edition__small">Corvane Nexus Platform</span><span class="edition__name">Healthcare Edition</span></span></div>
      <div class="edition" style="left:0;top:38px"><span class="edition__dot" style="background:var(--green)"></span><span><span class="edition__small">Corvane Nexus Platform</span><span class="edition__name">Nutrition &amp; Diet Edition</span></span></div>
      <div class="edition" style="left:160px;top:30px"><span class="edition__dot" style="background:var(--orange)"></span><span><span class="edition__small">Corvane Nexus Platform</span><span class="edition__name">Fitness Edition</span></span></div>
      <div class="edition" style="left:150px;top:64px"><span class="edition__dot" style="background:var(--blue)"></span><span><span class="edition__small">Corvane Nexus Platform</span><span class="edition__name">Pharma Edition</span></span></div>
      <div class="edition" style="left:300px;top:62px"><span class="edition__dot" style="background:var(--magenta)"></span><span><span class="edition__small">Corvane Nexus Platform</span><span class="edition__name">Ecommerce Edition</span></span></div>
    </div>

    <p class="body-text body-text--editions">Each Edition has a strategic architectural approach and a fine-tuned set of modules to provide a distinctive experience for each market. In addition, each Edition is built upon the Corvane Nexus Foundation Platform which offers the innovative triad of the Corvane Nexus Zo Ka Lum approach.</p>

    <h2 class="section-title section-title--why">WHY WE DO IT</h2>
    <p class="body-text body-text--why">The Corvane Nexus mission is to help each of our clients transfer their products, services and brands into the online and mobile realm without losing their brand messaging in translation. There's no point in having an app or a website just to have one. We take pride in bringing consumer-grade, enterprise level systems to the health and wellness industry. We embrace our clients' brand identities and mission statements, and join them in the goal to drive improved health outcomes and reduce costs.</p>

    <svg class="swoosh" style="top:522px" viewBox="0 0 540 40" aria-hidden="true"><path d="M40 8 Q270 40 500 30" fill="none" stroke="var(--light-gray)" stroke-width="4"/></svg>

    <p class="brand-small">corvane nexus</p>
    <address class="contact contact--head" style="font-style:normal">
      <span class="contact__label">Head Office:</span>
      Corvane Nexus, Inc.<br>48 Harbor Lane, Suite 210<br>Millbrook, NY 10990<br>Phone: (555) 014 2287<br>Fax: (555) 014 2290
    </address>
    <address class="contact contact--intl" style="font-style:normal">
      <span class="contact__label">International R&amp;D Office</span>
      Corvane Nexus<br>Orin Street #12<br>Tel Varen, Israel<br>Phone: +1 (555) 019 4410
    </address>
    <p class="contact-call">feel free to contact us</p>
    <p class="web">www.corvanenexus.com</p>
  </section>

  <section class="page page--cover">
    <h1 class="brand-cover">corvane nexus</h1>
    <p class="tagline">portal ecosystems and mobile applications<br>for clients in the health and wellness industry</p>
    <svg class="swoosh" style="top:196px" viewBox="0 0 540 40" aria-hidden="true"><path d="M50 10 Q280 36 500 24" fill="none" stroke="var(--light-gray)" stroke-width="4"/></svg>
    <div class="hero" role="img" aria-label="Photo of an apple sliced into layers of green apple, red apple and orange"></div>
    <div class="formula">
      <span class="formula__word">zo+ka+lum
        <svg width="18" height="14" viewBox="0 0 18 14" aria-hidden="true"><path d="M1 12 Q8 4 15 4 M11 1 L16 4 L12 8" fill="none" stroke="var(--dark-gray)" stroke-width="2"/></svg>
      </span>
      <p class="formula__note">learn more about our formula</p>
    </div>
  </section>

</main>
</body>
</html>
```